I need a poster to advertise the Prairie Crest Cup Soccer Tournament. It needs to incorporate the logo (attached). And the following information:
Save the Date!
7th Annual Prairie Crest Cup Soccer Tournament
April 27 - 29, 2018
Fernbrook Soccer Complex in Wichita, Kansas
30 - Natural Grass Soccer Fields
Recreational and Competitive
Boys and Girls U7 - U19
Website: www.tdkyfootie.example

I would like colors that go well with the blue in the tournament logo, but also add some excitement to the poster. Perhaps orange or purple or green?

You might also try some soccer artwork or background.

Font styles to use
Sans Serif

Colors
f37122
9bcb3c
6b449b

Requirements
Must have
• 7th Annual Prairie Crest Cup Soccer Tournament
• Save the Date
• April 27 - 29, 2018
• Fernbrook Soccer Complex
• Wichita, Kansas
• 30 - Natural Grass Soccer Fields
• Recreational and Competitive
• Boys and Girls U7 - U19
• Website: www.tdkyfootie.example
• Tournament logo
Nice to have
• Accent colors that go well with the blue in the tournament logo, but also add some contrast and energy. Perhaps orange, purple or green
• Soccer artwork
• Design elements that show action

```html
<!DOCTYPE html>
<html lang="en">
<head>
<meta charset="utf-8">
<title>7th Annual Prairie Crest Cup Soccer Tournament</title>
<link rel="stylesheet" href="https://fonts.googleapis.com/css2?family=Barlow+Condensed:wght@400;500;600;700&display=swap">
<style>
  :root {
    --ink: #1c1a1b;
    --white: #ffffff;
    --orange: #f37122;
    --green: #9bcb3c;
    --purple: #6b449b;
    --navy: #2f2787;
    --band-navy: #2c2a84;
    --shirt: #c81c1c;
    --shirt-dark: #7d0b0b;
    --sky: #f4e6e3;
    --crowd: #c9826f;
    --grass: #3f9a2e;
  }
  * { margin: 0; padding: 0; box-sizing: border-box; }
  html, body { width: 1200px; height: 800px; overflow: hidden; background: #fff; }
  body { font-family: "Barlow Condensed", "Arial Narrow", sans-serif; }

  .poster { position: relative; width: 1200px; height: 800px; overflow: hidden; }

  .stadium-photo {
    position: absolute; inset: 0;
    background: linear-gradient(180deg, var(--sky) 0%, #f1d6d0 30%, var(--crowd) 55%, #8c6a62 74%, #5a7a3a 86%, var(--grass) 100%);
  }
  .player-photo {
    position: absolute; left: 490px; top: 0; width: 710px; height: 800px;
    background: linear-gradient(90deg, rgba(200,28,28,0) 0%, rgba(200,28,28,0.85) 25%, var(--shirt) 45%, var(--shirt-dark) 100%);
  }

  .event-mark {
    position: absolute; left: 646px; top: 298px; width: 156px; height: 156px;
    border-radius: 50%; background: var(--white);
    display: flex; align-items: center; justify-content: center; text-align: center;
    color: var(--navy); font-weight: 700; font-size: 22px; line-height: 1;
  }

  .edition { position: absolute; left: 50px; top: 40px; color: var(--ink); font-weight: 500; font-size: 110px; line-height: 1; letter-spacing: 1px; }
  .edition sup { font-size: 46px; vertical-align: 50px; margin-left: 2px; margin-right: 14px; }
  .title { position: absolute; left: 51px; top: 152px; color: var(--ink); font-weight: 500; font-size: 62px; line-height: 66px; }

  .venue {
    position: absolute; left: 38px; top: 298px; width: 428px; height: 110px;
    background: var(--navy); color: var(--white);
    display: flex; flex-direction: column; justify-content: center; align-items: center;
    font-weight: 500; font-size: 38px; line-height: 42px;
  }

  .save-date { position: absolute; left: 51px; top: 476px; color: var(--ink); font-weight: 500; font-size: 88px; line-height: 1; -webkit-text-stroke: 1px rgba(255,255,255,0.6); }
  .dates {
    position: absolute; left: 56px; top: 566px; width: 390px; height: 78px;
    background: var(--orange); color: var(--white);
    font-weight: 700; font-size: 80px; line-height: 78px; text-align: center;
  }
  .year {
    position: absolute; left: 448px; top: 644px; transform-origin: 0 0; transform: rotate(-90deg);
    color: var(--ink); font-weight: 500; font-size: 46px; line-height: 46px; letter-spacing: 1px;
  }

  .info-band { position: absolute; left: 0; top: 662px; width: 780px; height: 96px; }
  .info-band svg { position: absolute; inset: 0; }
  .info { position: absolute; top: 0; height: 96px; display: flex; flex-direction: column; justify-content: center; color: var(--white); font-weight: 700; line-height: 1; }
  .info-fields { left: 18px; }
  .info-fields .big { font-size: 50px; }
  .info-fields .small { font-size: 29px; margin-top: 2px; }
  .info-level { left: 325px; font-size: 34px; line-height: 36px; }
  .info-ages { left: 580px; }
  .info-ages .small { font-size: 32px; }
  .info-ages .big { font-size: 56px; margin-top: -2px; }

  .website { position: absolute; left: 948px; top: 737px; display: flex; align-items: center; gap: 6px; color: var(--white); font-weight: 500; font-size: 24px; }
</style>
</head>
<body>
<main class="poster">
  <div class="stadium-photo" role="img" aria-label="Blurred stadium crowd under bright lights above a green pitch"></div>
  <div class="player-photo" role="img" aria-label="Player in a red number 7 jersey holding a soccer ball against the hip, seen from the side"></div>

  <div class="event-mark">Prairie<br>Crest Cup</div>

  <h1 class="edition">7<sup>th</sup>ANNUAL</h1>
  <p class="title">Prairie Crest Cup<br>Soccer Tournament</p>

  <div class="venue"><span>Fernbrook Soccer Complex</span><span>WICHITA, KANSAS</span></div>

  <p class="save-date">SAVE THE DATE</p>
  <div class="dates">APRIL 27-29</div>
  <div class="year">2018</div>

  <section class="info-band">
    <svg width="780" height="96" viewBox="0 0 780 96" aria-hidden="true">
      <polygon points="0,0 322,0 300,48 322,96 0,96" fill="var(--orange)"/>
      <polygon points="322,0 590,0 568,48 590,96 322,96 300,48" fill="var(--green)"/>
      <polygon points="590,0 758,0 780,96 590,96 568,48" fill="var(--band-navy)"/>
    </svg>
    <div class="info info-fields"><span class="big">30-NATURAL</span><span class="small">Grass Soccer Fields</span></div>
    <div class="info info-level"><span>Recreational &amp;</span><span>COMPETITIVE</span></div>
    <div class="info info-ages"><span class="small">Boys &amp; Girls</span><span class="big">U7-U19</span></div>
  </section>

  <div class="website">
    <svg width="16" height="16" viewBox="0 0 16 16" aria-hidden="true" fill="none" stroke="#fff" stroke-width="1.3">
      <circle cx="8" cy="8" r="7"/><ellipse cx="8" cy="8" rx="3" ry="7"/><line x1="1" y1="8" x2="15" y2="8"/>
    </svg>
    <span>www.tdkyfootie.example</span>
  </div>
</main>
</body>
</html>
```